Stellenanzeigen zur Mitarbeitergewinnung über soziale Medien & Google / YouTube
Zielgruppe
Wir sind zwei Brüder und Inhaber der Zahnarztpraxis „ Zahnmedizin im Lindenquartier“ in Bochum.
Wir benötigen zur Mitarbeitergewinnung ein neues, modernes Konzept. Insbesondere stehen Stellenanzeigen im Vordergrund, die in sozialen Medien, wie Instagram, aber auch über Google und YouTube angezeigt werden sollen und potentielle Mitarbeiter auf unsere eigene Landingpage zur Mitarbeitergewinnung führen
Es geht nicht darum, Patienten anzusprechen, sondern ausschließlich um Mitarbeitergewinnung.
Aufgabenstellung
Wir haben Interesse an einem Gesamtkonzept, eine Serie von Anzeigen, die unsere Praxis widerspiegeln, uns als Inhaber zeigen, sowie unsere vorhandenen Mitarbeiterinnen einbinden.
Aufgrund der Vielzahl von Stellenanzeigen im medizinischen Bereich, braucht es neue Ideen. Wir möchten uns deutlich von den vorhandenen, unzähligen Anzeigen bei Instagram abheben. Hier sind kreative Ideen erwünscht.
Wir haben eine zur Mitarbeitergewinnung vorhandene Homepage, die Videos und Aussagekräftige Fotos und Texte beinhaltet. Dort gibt es die Möglichkeit, sich direkt auf eine freie Stelle unkompliziert zu bewerben.
Wir möchten über die neuen Anzeigen potentielle Mitarbeiter dazu bewegen, sich diese Homepage anzusehen und sich gegebenfalls direkt zu bewerben.
Wir freuen uns über ein Gesamtkonzept, gerne verschiedene Stellenanzeigen, die aber ineinander schlüssig sind. Beispielsweise mit anderen Überschriften oder mit verschiedenen Fotos, die wir bereitstellen. Die vorgeschlagenen Fotos können gerne benutzt werden, alternativ sind wir im Hinblick auf das Gesamtkonzept auch offen für andere Ideen und Fotos. Da die Mitbewerbersituation extrem hoch ist, macht es Sinn, sich vorhandene Stellenanzeigen anzusehen, damit wir deutlich die Vorteile unserer Praxis transportieren und uns klar positionieren.
Wir Inhaber, Brüder, Dr. Tobias und Jörg Wessling, sind Ende 30, Ruhrpottkinder, haben eine moderne Praxis zentral in Bochum am Auhof.
Unsere Praxis ist im modernen und ansprechenden Lindenquartier. Wir haben bereits ein großes Team und zwei weitere angestellte Zahnärztinnen. Bei uns gibt es eine faire Bezahlung, Zusatzleistungen, die eine Gutscheinkarte oder die Möglichkeit eines Stellplatzes oder ÖPNV Ticket. Wir machen keine Überstunden, sind freundliche und entspannte Chefs. Wir legen Wert auf Qualität und nehmen uns für uns Zeit für Patienten und Mitarbeiter.
Ziel sollte es sein, motivierte und leistungsstarke Mita..

```html
<!DOCTYPE html>
<html lang="de">
<head>
<meta charset="utf-8">
<title>Stellenanzeige – Stagnation ist nicht dein Stil?</title>
<link rel="stylesheet" href="https://fonts.googleapis.com/css2?family=Gochi+Hand&family=Baloo+2:wght@800&family=Arimo:wght@400;700&display=swap">
<style>
  :root {
    --stage: #6f7384;
    --green-light: #93ca57;
    --green-mid: #86b055;
    --green-dark: #5e9632;
    --green-deep: #6a9a3c;
    --beige: #ddd6aa;
    --beige-dark: #c9c08e;
    --olive-text: #6f6a3e;
    --white: #ffffff;
    --ink: #1d1d1f;
    --badge: #4a78d4;
  }
  html, body {
    margin: 0;
    padding: 0;
    width: 1200px;
    height: 2380px;
    overflow: hidden;
    background: var(--stage);
  }
  .ad-post {
    position: absolute;
    left: 50px;
    top: 640px;
    width: 1100px;
    height: 1100px;
    display: block;
    box-shadow: 0 10px 30px rgba(0,0,0,.25);
  }
  .headline-main, .headline-sub {
    font-family: "Gochi Hand", cursive;
    fill: var(--green-dark);
  }
  .headline-main { font-size: 140px; }
  .headline-sub { font-size: 96px; }
  .challenge-line {
    font-family: "Baloo 2", sans-serif;
    font-weight: 800;
    font-size: 56px;
    fill: var(--white);
    stroke: var(--green-dark);
    stroke-width: 6px;
    paint-order: stroke;
  }
  .cta-label {
    font-family: "Arimo", sans-serif;
    font-weight: 700;
    font-size: 42px;
    fill: var(--olive-text);
    letter-spacing: -1px;
  }
  .cta-sub {
    font-family: "Arimo", sans-serif;
    font-weight: 700;
    font-size: 34px;
    fill: var(--green-deep);
    letter-spacing: -1.5px;
  }
  .practice-name {
    font-family: "Arimo", sans-serif;
    font-weight: 400;
    font-size: 17px;
    fill: var(--ink);
  }
  .practice-owners {
    font-family: "Arimo", sans-serif;
    font-weight: 400;
    font-size: 7px;
    fill: var(--ink);
  }
  .listing-note {
    font-family: "Arimo", sans-serif;
    font-weight: 700;
    font-size: 13px;
    fill: var(--ink);
    letter-spacing: -0.5px;
  }
</style>
</head>
<body>
<svg class="ad-post" viewBox="0 0 1026 1026" xmlns="http://www.w3.org/2000/svg">
  <defs>
    <linearGradient id="bg-green" x1="0" y1="0" x2="1" y2="1">
      <stop offset="0" stop-color="var(--green-light)"/>
      <stop offset="1" stop-color="var(--green-mid)"/>
    </linearGradient>
    <linearGradient id="portrait-tone" x1="0" y1="0" x2="0" y2="1">
      <stop offset="0" stop-color="#2a2522"/>
      <stop offset="0.3" stop-color="#b98f78"/>
      <stop offset="0.5" stop-color="#1e1e1e"/>
      <stop offset="1" stop-color="#121212"/>
    </linearGradient>
  </defs>

  <!-- background -->
  <rect class="backdrop" width="1026" height="1026" fill="url(#bg-green)"/>

  <!-- wave bands -->
  <path class="wave-beige" fill="var(--beige)"
        d="M0 705 C60 675 120 665 180 672 C260 684 310 645 370 616 C440 584 480 610 550 582 C610 556 650 524 720 524 C800 524 840 486 900 470 C950 458 990 476 1026 474 L1026 1026 L0 1026 Z"/>
  <path class="wave-white" fill="var(--white)"
        d="M0 755 C60 720 120 706 180 716 C260 728 300 696 360 666 C430 632 470 658 540 628 C600 602 640 576 710 576 C790 576 830 536 890 522 C940 512 990 530 1026 530 L1026 1026 L0 1026 Z"/>

  <!-- speech bubble -->
  <path class="bubble-shadow" fill="var(--green-dark)"
        d="M175 80 L840 40 C900 38 905 70 905 120 L895 320 C890 365 860 378 820 384 C790 390 770 400 772 425 C740 415 715 412 650 415 L240 440 C190 443 170 425 160 390 L120 190 C110 120 130 85 175 80 Z" transform="translate(6 16)"/>
  <path class="bubble" fill="var(--beige)" stroke="var(--white)" stroke-width="6"
        d="M175 80 L840 40 C900 38 905 70 905 120 L895 320 C890 365 860 378 820 384 C790 390 770 400 772 425 C740 415 715 412 650 415 L240 440 C190 443 170 425 160 390 L120 190 C110 120 130 85 175 80 Z"/>

  <g transform="rotate(-6 520 250)">
    <text class="headline-main" x="522" y="250" text-anchor="middle" textLength="600" lengthAdjust="spacingAndGlyphs">Stagnation</text>
    <text class="headline-sub" x="522" y="352" text-anchor="middle" textLength="610" lengthAdjust="spacingAndGlyphs">ist nicht dein Stil?</text>
  </g>

  <!-- subline -->
  <g transform="rotate(-4 372 555)">
    <text class="challenge-line" x="372" y="532" text-anchor="middle" textLength="585" lengthAdjust="spacingAndGlyphs">Hier wartet die nächste</text>
    <text class="challenge-line" x="372" y="585" text-anchor="middle" textLength="405" lengthAdjust="spacingAndGlyphs">Herausforderung</text>
  </g>

  <!-- portrait placeholder -->
  <path class="portrait" role="img" aria-label="Porträtfoto einer lächelnden Mitarbeiterin mit langen dunklen Haaren im schwarzen Oberteil"
        fill="url(#portrait-tone)"
        d="M540 1026 C545 880 580 780 660 745 C680 650 690 520 730 470 C760 432 815 432 845 470 C880 520 885 650 905 745 C975 780 1000 880 1000 1026 Z"/>

  <!-- call to action -->
  <rect class="cta-shadow" x="137" y="756" width="315" height="64" rx="32" fill="var(--beige-dark)"/>
  <rect class="cta-button" x="137" y="747" width="315" height="62" rx="31" fill="var(--beige)"/>
  <text class="cta-label" x="294" y="793" text-anchor="middle">Klick Sie hier</text>
  <text class="cta-sub" x="294" y="872" text-anchor="middle">Erhalte mehr Infos!</text>

  <!-- practice name -->
  <rect class="practice-mark" x="140" y="896" width="26" height="26" fill="var(--beige-dark)"/>
  <text class="practice-name" x="92" y="946">Zahnmedizin</text>
  <text class="practice-name" x="92" y="963">im Lindenquartier</text>
  <text class="practice-owners" x="92" y="984">Dr. Tobias &amp; Jörg Wessling mit Team</text>

  <!-- listing badge -->
  <rect class="listing-badge" x="242" y="935" width="54" height="52" rx="6" fill="var(--badge)"/>
  <text class="listing-note" x="309" y="965">Wir sind auch bei</text>
  <text class="listing-note" x="309" y="983">Ortsfinder gelistet</text>
</svg>
</body>
</html>
```